Retractable Banners Designs for Tradeshows

We like the look and feel of the banners draft but want a more polished and improved version of the banners

The dimensions of each banner should be 33" x 80"

We want the banners to work on their own as they will be used in different places, but at tradeshows, they might be used side by side in a 10x10 tradeshow booth, so common design elements that work together is needed.
Updates

Low design quality

Target Market(s)

tradeshows booths

Colors
EB3D1F
EC4F4E
F09395
F8D3D4
FCEDEE

Requirements
Must have
• Elements that tie all the banners together, large scale images, not to cluttered or busy, designed to be visible and attractive from far away, our corporate colours are red, black, white and gray
Nice to have
• bright design not dark but using our corporate colours of red, gray, white and some black

```html
<!DOCTYPE html>
<html lang="en">
<head>
<meta charset="utf-8">
<title>Nexalink Retractable Banner Set</title>
<link href="https://fonts.googleapis.com/css2?family=Arimo:wght@400;700&display=swap" rel="stylesheet">
<style>
  :root {
    --red: #e0141b;
    --red-dark: #7a0a0c;
    --black: #111111;
    --white: #ffffff;
    --page: #d5d2d2;
    --ink: #1a1a1a;
  }
  * { margin: 0; padding: 0; box-sizing: border-box; }
  html, body { width: 849px; height: 1200px; overflow: hidden; }
  body {
    background: var(--page);
    font-family: "Arimo", Arial, sans-serif;
    display: flex;
    align-items: center;
    justify-content: center;
  }
  .banner-set { display: flex; gap: 8px; }
  .banner {
    position: relative;
    width: 196px;
    height: 475px;
    background: var(--white);
    overflow: hidden;
    box-shadow: 0 2px 6px rgba(0,0,0,0.15);
  }
  .banner-shapes { position: absolute; inset: 0; width: 196px; height: 475px; }
  .brand {
    position: absolute;
    top: 36px; left: 0; right: 0;
    display: flex; align-items: center; justify-content: center; gap: 6px;
    color: var(--white);
    font-size: 23px; font-weight: 400; letter-spacing: 0.2px;
  }
  .brand-dot { width: 9px; height: 9px; border-radius: 50%; background: var(--white); }
  .category {
    position: absolute;
    top: 348px; left: 0; right: 0;
    height: 30px;
    display: flex; align-items: center; justify-content: center;
    color: var(--white);
    font-size: 11px; font-weight: 700; line-height: 1.05;
    text-transform: uppercase; text-align: center; letter-spacing: 0.3px;
  }
  .tagline {
    position: absolute;
    top: 385px; left: 8px; right: 8px;
    color: var(--ink);
    font-size: 11.5px; line-height: 1.35; text-align: center;
  }
  .site-url {
    position: absolute;
    top: 437px; left: 0; right: 0;
    height: 18px; line-height: 18px;
    color: var(--white);
    font-size: 10.5px; text-align: center;
  }
</style>
</head>
<body>
<svg width="0" height="0" style="position:absolute" aria-hidden="true">
  <defs>
    <linearGradient id="tab-fill" x1="0" x2="1" y1="0" y2="0">
      <stop offset="0" stop-color="#e0141b"/><stop offset="1" stop-color="#7a0a0c"/>
    </linearGradient>
    <linearGradient id="photo-tower" x1="0" y1="0" x2="0" y2="1">
      <stop offset="0" stop-color="#3a6dbb"/><stop offset="0.55" stop-color="#7a93b8"/><stop offset="1" stop-color="#24272c"/>
    </linearGradient>
    <linearGradient id="photo-racks" x1="0" y1="0" x2="1" y2="1">
      <stop offset="0" stop-color="#6f8196"/><stop offset="0.5" stop-color="#2b3746"/><stop offset="1" stop-color="#1a2230"/>
    </linearGradient>
    <linearGradient id="photo-bench" x1="0" y1="0" x2="0" y2="1">
      <stop offset="0" stop-color="#8e8a84"/><stop offset="0.5" stop-color="#4a4845"/><stop offset="1" stop-color="#2a2927"/>
    </linearGradient>
    <linearGradient id="photo-field" x1="0" y1="0" x2="1" y2="0">
      <stop offset="0" stop-color="#c9c7c3"/><stop offset="0.6" stop-color="#a8928a"/><stop offset="1" stop-color="#d8d6d3"/>
    </linearGradient>
  </defs>
</svg>

<main class="banner-set">
  <!-- Banner 1 -->
  <section class="banner">
    <svg class="banner-shapes" viewBox="0 0 196 475">
      <path d="M0 0H196V80Q100 66 0 94Z" fill="var(--red)"/>
      <path d="M0 0H78Q30 8 0 24Z" fill="var(--black)"/>
      <path d="M0 104Q100 76 196 88V332Q100 348 0 372Z" fill="url(#photo-tower)" role="img" aria-label="Photo of a telecom tower with antennas against a blue sky"/>
      <path d="M0 94Q100 68 196 80V88Q100 76 0 104Z" fill="var(--white)"/>
      <path d="M0 372Q100 348 196 332V342Q100 358 0 384Z" fill="var(--red)"/>
      <path d="M0 384Q100 358 196 342V346Q100 362 0 388Z" fill="var(--black)"/>
      <path d="M30 346H168L160 378H22Z" fill="url(#tab-fill)"/>
      <rect x="0" y="437" width="196" height="18" fill="var(--red)"/>
      <path d="M0 455H196V475H0Z" fill="var(--white)"/>
      <path d="M0 458Q110 460 196 475H0Z" fill="var(--black)"/>
    </svg>
    <div class="brand"><span class="brand-dot"></span>Nexalink</div>
    <div class="category">Telecom<br>Infrastructure</div>
    <p class="tagline">Cutting Edge<br>Solutions for the<br>Next Generation</p>
    <div class="site-url">www.nexalink.com</div>
  </section>

  <!-- Banner 2 -->
  <section class="banner">
    <svg class="banner-shapes" viewBox="0 0 196 475">
      <path d="M0 0H196V68Q100 72 0 88Z" fill="var(--red)"/>
      <path d="M0 96Q100 80 196 76V338Q100 350 0 364Z" fill="url(#photo-racks)" role="img" aria-label="Photo of server racks with network equipment"/>
      <path d="M0 88Q100 72 196 68V76Q100 80 0 96Z" fill="var(--white)"/>
      <path d="M0 364Q100 350 196 338V346Q100 360 0 374Z" fill="var(--red)"/>
      <path d="M0 374Q100 360 196 346V350Q100 364 0 378Z" fill="var(--black)"/>
      <path d="M30 346H168L160 376H22Z" fill="url(#tab-fill)"/>
      <rect x="0" y="437" width="196" height="18" fill="var(--red)"/>
      <path d="M0 460Q110 462 196 475H0Z" fill="var(--black)"/>
    </svg>
    <div class="brand"><span class="brand-dot"></span>Nexalink</div>
    <div class="category">ICT Solutions</div>
    <p class="tagline">Seamless Cable and<br>Telecom Networks and<br>Enterprise Deployments</p>
    <div class="site-url">www.nexalink.com</div>
  </section>

  <!-- Banner 3 -->
  <section class="banner">
    <svg class="banner-shapes" viewBox="0 0 196 475">
      <path d="M0 0H196V68Q100 64 0 68Z" fill="var(--red)"/>
      <path d="M0 76Q100 70 196 76V330Q100 344 0 352Z" fill="url(#photo-bench)" role="img" aria-label="Photo of test and measurement instruments on a lab bench"/>
      <path d="M0 68Q100 64 196 68V76Q100 70 0 76Z" fill="var(--white)"/>
      <path d="M0 352Q100 344 196 330V338Q100 354 0 362Z" fill="var(--red)"/>
      <path d="M0 362Q100 354 196 338V342Q100 358 0 366Z" fill="var(--black)"/>
      <path d="M30 346H168L160 378H22Z" fill="url(#tab-fill)"/>
      <rect x="0" y="437" width="196" height="18" fill="var(--red)"/>
      <path d="M0 460Q110 462 196 475H0Z" fill="var(--black)"/>
    </svg>
    <div class="brand"><span class="brand-dot"></span>Nexalink</div>
    <div class="category">Test &amp;<br>Measurement</div>
    <p class="tagline">Accurate and<br>Efficient Solutions<br>for the Wireless World</p>
    <div class="site-url">www.nexalink.com</div>
  </section>

  <!-- Banner 4 -->
  <section class="banner">
    <svg class="banner-shapes" viewBox="0 0 196 475">
      <path d="M0 0H196V60Q100 70 0 80Z" fill="var(--red)"/>
      <path d="M150 0H196V12Q175 4 150 0Z" fill="var(--black)"/>
      <path d="M0 88Q100 78 196 68V250Q100 296 0 320Z" fill="url(#photo-field)" role="img" aria-label="Photo of a technician in a hard hat installing RF hardware on a mast"/>
      <path d="M0 80Q100 70 196 60V68Q100 78 0 88Z" fill="var(--white)"/>
      <path d="M0 320Q100 296 196 250V272Q100 310 0 330Z" fill="var(--red)"/>
      <path d="M0 330Q100 310 196 272V296Q100 330 0 340Z" fill="var(--black)"/>
      <path d="M30 346H168L160 376H22Z" fill="url(#tab-fill)"/>
      <rect x="0" y="437" width="196" height="18" fill="var(--red)"/>
      <path d="M0 460Q110 462 196 475H0Z" fill="var(--black)"/>
    </svg>
    <div class="brand"><span class="brand-dot"></span>Nexalink</div>
    <div class="category">Hardware</div>
    <p class="tagline">High-Quality, Economical,<br>Test Grade RF and<br>Microwave Components</p>
    <div class="site-url">www.nexalink.com</div>
  </section>
</main>
</body>
</html>
```